I need a business card design for a new company that will be doing consulting work around issues of cultural competency, and diversity and inclusion. I would like the design to be crisp and clear with bold but conservative colors and incorporate shades of blue

Target Market(s)

Small businesses, schools, non-profits

Industry/Entity Type

Consulting

Font styles to use
Serif
Sans Serif

Colors
0c5ba6
6b449b
3276b5
0292cd

Requirements
Must have
• A Morrow Venture (name of company)
• Lemlem Tavish
• CEO
• lemlem@amorrowventure.com
• (215)483-2756

```html
<!DOCTYPE html>
<html lang="en">
<head>
<meta charset="utf-8">
<title>A Morrow Venture – Business Card</title>
<link rel="stylesheet" href="https://fonts.googleapis.com/css2?family=Barlow:wght@400;500;600&display=swap">
<style>
  :root{
    --backdrop:#35b46f;
    --card-blue:#115ca8;
    --sidebar-blue:#0894cd;
    --rule-green:#2aa57a;
    --rule-blue:#2e5fa0;
    --white:#ffffff;
  }
  *{margin:0;padding:0;box-sizing:border-box}
  html,body{width:1200px;height:1200px;overflow:hidden;background:var(--backdrop)}
  body{position:relative;font-family:"Barlow",Arial,sans-serif;color:var(--white)}

  .card{position:absolute;width:900px;height:540px;background:var(--card-blue);overflow:hidden}
  .card--front{left:27px;top:31px}
  .card--back{left:270px;top:633px}

  .brand{position:absolute;display:flex;flex-direction:column;align-items:center;transform:translateX(-50%)}
  .brand__mark{background:var(--white);border-radius:50%}
  .brand__name{font-weight:600;white-space:nowrap;letter-spacing:.5px}

  .card--front .brand{left:451px;top:148px}
  .card--front .brand__mark{width:176px;height:176px}
  .card--front .brand__name{font-size:38px;margin-top:36px}

  .card--back .brand{left:730px;top:97px}
  .card--back .brand__mark{width:112px;height:112px}
  .card--back .brand__name{font-size:23px;margin-top:18px}

  .sidebar{position:absolute;left:0;top:0;width:81px;height:100%;background:var(--sidebar-blue)}
  .person-icon{position:absolute;left:29px;top:95px;width:40px;height:40px}

  .identity{position:absolute;left:98px;top:90px}
  .identity__name{font-size:37px;font-weight:600;letter-spacing:.5px;line-height:1}
  .identity__title{font-size:21px;font-weight:400;letter-spacing:1px;margin-top:14px}

  .contacts{position:absolute;left:0;top:274px;width:416px;list-style:none;border-top:2px solid var(--rule-blue)}
  .contact{position:relative;display:flex;align-items:center;height:36px;font-size:21px;letter-spacing:.6px}
  .contact:last-child{height:40px}
  .contact::after{content:"";position:absolute;left:81px;right:0;bottom:0;height:1px;background:var(--rule-green)}
  .contact::before{content:"";position:absolute;left:0;width:81px;bottom:0;height:2px;background:var(--rule-blue)}
  .contact__icon{width:81px;display:flex;justify-content:center}
  .contact__icon svg{width:20px;height:20px}
  .contact__text{padding-left:15px}
</style>
</head>
<body>

<section class="card card--front">
  <div class="brand">
    <div class="brand__mark"></div>
    <div class="brand__name">A Morrow Venture</div>
  </div>
</section>

<section class="card card--back">
  <div class="sidebar"></div>
  <svg class="person-icon" viewBox="0 0 40 40" aria-hidden="true">
    <circle cx="20" cy="11" r="9" fill="#fff"/>
    <path d="M2 40 C2 27 10 22 20 22 C30 22 38 27 38 40 Z" fill="#fff"/>
  </svg>

  <div class="identity">
    <div class="identity__name">Lemlem Tavish</div>
    <div class="identity__title">CEO</div>
  </div>

  <ul class="contacts">
    <li class="contact">
      <span class="contact__icon"><svg viewBox="0 0 24 24"><path fill="#fff" d="M6.6 10.8c1.4 2.8 3.8 5.1 6.6 6.6l2.2-2.2c.3-.3.7-.4 1-.2 1.1.4 2.3.6 3.6.6.6 0 1 .4 1 1V20c0 .6-.4 1-1 1C10.6 21 3 13.4 3 4c0-.6.4-1 1-1h3.5c.6 0 1 .4 1 1 0 1.3.2 2.5.6 3.6.1.3 0 .7-.2 1z"/><path d="M14 3a7 7 0 0 1 7 7M14 6.5a3.5 3.5 0 0 1 3.5 3.5" stroke="#fff" stroke-width="1.8" fill="none"/></svg></span>
      <span class="contact__text">(215) 483-2756</span>
    </li>
    <li class="contact">
      <span class="contact__icon"><svg viewBox="0 0 24 24"><rect x="3" y="6" width="18" height="13" rx="1" fill="#fff"/><path d="M3 7l9 6 9-6" stroke="#0894cd" stroke-width="1.6" fill="none"/></svg></span>
      <span class="contact__text">lemlem@amorrowventure.com</span>
    </li>
    <li class="contact">
      <span class="contact__icon"><svg viewBox="0 0 24 24" fill="none" stroke="#fff" stroke-width="1.6"><circle cx="12" cy="12" r="9"/><ellipse cx="12" cy="12" rx="4" ry="9"/><path d="M3 12h18M5 7h14M5 17h14"/></svg></span>
      <span class="contact__text">amorrowventure.com</span>
    </li>
    <li class="contact">
      <span class="contact__icon"><svg viewBox="0 0 24 24"><path fill="#fff" d="M12 2a7 7 0 0 0-7 7c0 5 7 13 7 13s7-8 7-13a7 7 0 0 0-7-7z"/><circle cx="12" cy="9" r="2.6" fill="#0894cd"/></svg></span>
      <span class="contact__text">Location</span>
    </li>
  </ul>

  <div class="brand">
    <div class="brand__mark"></div>
    <div class="brand__name">A Morrow Venture</div>
  </div>
</section>

</body>
</html>
```